House Builder and Property Development Card Design and Logo

I need a business card design for a building and property development company.
Colour scheme of Dark Grey and Green, I would like it bold, sharp and professional.
No logo yet done, I'm open to options but please stay away from the usual- house, roof, hammers etc.
Thanks Rob

Please be aware that on the business card information section the WHRC # 5528391 is a licence number and my phone number 0492837165. The numbers are close together and could be mistaken as one whole number 

Thank you

                                   

Industry/Entity Type

Building

Contact Information for Business Card

VARGA BUILD & DEVELOPMENT.
Residential Building & Property Development
Robert Varga - Director
WHRC # 5528391
0492837165
rob@vargabuild.example.com.au

Requirements
Must have
• Bold Business name
Dark grey and green colours
Should not have
• roof outline or hammer logo

```html
<!DOCTYPE html>
<html lang="en">
<head>
<meta charset="utf-8">
<title>Varga Build &amp; Development – Business Card</title>
<link rel="stylesheet" href="https://fonts.googleapis.com/css2?family=PT+Sans+Narrow:wght@400;700&display=swap">
<style>
  :root {
    --backdrop: #2b2a2a;
    --card-dark: #1f1f1f;
    --card-light: #ffffff;
    --brand-green: #9ccb2e;
    --text-light: #f2f2f2;
    --text-dark: #1e1e1e;
    --muted: #bdbdbd;
  }
  * { margin: 0; padding: 0; box-sizing: border-box; }
  html, body {
    width: 1200px;
    height: 873px;
    overflow: hidden;
    background: var(--backdrop);
    font-family: "PT Sans Narrow", "Arial Narrow", sans-serif;
  }
  .canvas {
    position: relative;
    width: 1200px;
    height: 873px;
    display: flex;
    align-items: center;
    justify-content: center;
    gap: 60px;
  }
  .card {
    position: relative;
    width: 520px;
    height: 297px;
    border-radius: 3px;
    box-shadow: 0 10px 30px rgba(0,0,0,0.45);
    overflow: hidden;
  }

  /* Information side */
  .card--info {
    background: linear-gradient(160deg, #262626 0%, var(--card-dark) 100%);
    color: var(--text-light);
  }
  .holder {
    position: absolute;
    left: 34px;
    top: 30px;
  }
  .holder__name {
    font-weight: 700;
    font-size: 26px;
    letter-spacing: 0.3px;
    color: var(--text-light);
  }
  .holder__role {
    font-size: 14px;
    color: var(--brand-green);
    margin-top: 2px;
  }
  .contact {
    position: absolute;
    left: 34px;
    top: 112px;
    list-style: none;
    font-size: 14px;
    line-height: 1.6;
  }
  .contact__label { color: var(--brand-green); }
  .contact__value { color: var(--text-light); }
  .company {
    position: absolute;
    right: 30px;
    bottom: 34px;
    text-align: right;
  }
  .company__name {
    font-weight: 700;
    font-size: 28px;
    color: var(--brand-green);
    letter-spacing: 0.4px;
  }
  .company__tagline {
    font-size: 15px;
    color: var(--text-light);
    margin-top: 1px;
  }

  /* Brand side */
  .card--brand {
    background: var(--card-light);
    display: flex;
    align-items: center;
    justify-content: center;
  }
  .brand {
    display: flex;
    align-items: center;
    gap: 14px;
  }
  .brand__square {
    width: 22px;
    height: 22px;
    background: var(--brand-green);
  }
  .brand__name {
    font-weight: 700;
    font-size: 30px;
    color: var(--text-dark);
    letter-spacing: 0.4px;
  }
  .brand__tagline {
    font-size: 15px;
    color: var(--brand-green);
    margin-top: 2px;
  }
</style>
</head>
<body>
<main class="canvas">
  <section class="card card--info" aria-label="Business card, contact side">
    <div class="holder">
      <p class="holder__name">Robert Varga</p>
      <p class="holder__role">Director</p>
    </div>
    <ul class="contact">
      <li><span class="contact__label">Licence no:</span> <span class="contact__value">WHRC # 5528391</span></li>
      <li><span class="contact__label">Phone no:</span> <span class="contact__value">0492 837 165</span></li>
      <li><span class="contact__label">Email:</span> <span class="contact__value">rob@vargabuild.example.com.au</span></li>
    </ul>
    <div class="company">
      <p class="company__name">VARGA BUILD &amp; DEVELOPMENT</p>
      <p class="company__tagline">Residential Building &amp; Property Development</p>
    </div>
  </section>

  <section class="card card--brand" aria-label="Business card, brand side">
    <div class="brand">
      <span class="brand__square" aria-hidden="true"></span>
      <div>
        <p class="brand__name">VARGA BUILD &amp; DEVELOPMENT</p>
        <p class="brand__tagline">Residential Building &amp; Property Development</p>
      </div>
    </div>
  </section>
</main>
</body>
</html>
```